Thai Menu Design Project

We need a new menu design for a Thai restaurant in Fort Worth, Texas. We are a family-owned and really proud about our food and our service. We want the menu to feel healthy, modern, delicious, artistic Thai, and friendly. The colors we used in our restaurant are maroon, burgundy, black, white, gold and pale yellow.

Please look at our website www.brindlewokery.com
for the reference of the menus and the photos we use.

The menu can be in any number of pages (the fewer the better though) The size of the paper is US letter.
Updates

Update:

- We don't put the photos of the food in the menu pages anymore, instead, we like to put the photos of the herbs and their benefits (found in the file 'herb benefits') on the menu pages instead.

- the paper size is US letter.

- we don't have specific numbers of pages but the fewer the better

Thank you!

I added logos and background photo again in case the previous files did not work. Thanks!

Target Market(s)

Trendy socialized people from 20-30s,couples of all ages from 20s-60s,and families.

Industry/Entity Type

Restaurant

Requirements
Must have
• We want the menu to feel healthy, modern, delicious, artistic, Thai, and friendly.

We like to keep the colors maroon, burgundy, black, gold, pale yellow, and off white.

We like to put the photos of the herbs and their benefits (available in the file called 'herb benefits') randomly in the menu pages.

*Please use the photos available in the file called 'herb benefits' along with its details somewhere in the pages. You can change the photo of each herb to the ones you find more fitting from the internet.

Nice to have
• If we can add the wallpaper pattern in our menu it will be great. It can be used in anyway.

```html
<!DOCTYPE html>
<html lang="en">
<head>
<meta charset="utf-8">
<title>Brindle Wokery – Appetizers Menu</title>
<link href="https://fonts.googleapis.com/css2?family=Sorts+Mill+Goudy&family=Open+Sans:wght@300;400&family=Great+Vibes&display=swap" rel="stylesheet">
<style>
  :root{
    --cream:#fdf8dc;
    --cream-light:#fffcea;
    --maroon:#7a0d0d;
    --red-dark:#8e0a0a;
    --red:#c4161c;
    --red-bright:#e01a1a;
    --gold-light:#fbf2b0;
    --gold:#d8c06a;
    --gold-dark:#a88a2e;
    --ink:#5a4a3a;
    --white:#ffffff;
  }
  *{margin:0;padding:0;box-sizing:border-box;}
  html,body{width:1200px;height:854px;overflow:hidden;}
  body{background:var(--cream);}
  .menu-spread{
    position:relative;width:1200px;height:854px;overflow:hidden;
    background:linear-gradient(90deg,var(--cream-light) 0%,var(--cream) 55%,#fcf6cf 100%);
    font-family:"Open Sans",sans-serif;
  }
  /* Left page */
  .brand-top{position:absolute;left:156px;top:48px;width:284px;text-align:center;}
  .brand-top .brand-name{
    font-family:"Sorts Mill Goudy",serif;font-size:36px;color:var(--maroon);line-height:1;
  }
  .brand-top .brand-tagline{font-size:11px;color:var(--maroon);margin-top:6px;letter-spacing:.3px;}
  .feature-photo{position:absolute;left:134px;top:202px;width:332px;height:332px;}
  .photo-shadow{
    position:absolute;left:204px;top:548px;width:192px;height:12px;border-radius:50%;
    background:radial-gradient(ellipse at center,rgba(120,110,90,.35) 0%,rgba(120,110,90,0) 70%);
  }
  .brand-panel{
    position:absolute;left:0;top:590px;width:600px;height:264px;
    background:radial-gradient(ellipse at 35% 25%,var(--red-bright) 0%,var(--red) 35%,var(--red-dark) 100%);
  }
  .brand-panel .brand-name{
    position:absolute;left:0;width:600px;top:90px;text-align:center;
    font-family:"Sorts Mill Goudy",serif;font-size:44px;color:var(--white);line-height:1;
  }
  .brand-panel .brand-tagline{
    position:absolute;left:0;width:600px;top:142px;text-align:center;
    font-size:15px;font-weight:300;color:var(--white);
  }
  /* Right page */
  .section-banner{position:absolute;left:764px;top:32px;width:272px;height:86px;}
  .section-title{
    position:absolute;left:764px;top:46px;width:272px;text-align:center;
    font-family:"Great Vibes",cursive;font-size:28px;line-height:1.2;color:var(--white);
    transform:rotate(4deg);
  }
  .menu-item{position:absolute;width:240px;}
  .item-bar{
    position:relative;height:46px;
    background:linear-gradient(90deg,var(--red-dark) 0%,var(--red) 60%,var(--red-bright) 100%);
    box-shadow:0 0 0 1px rgba(216,192,106,.55),1px 2px 3px rgba(0,0,0,.25);
    display:flex;flex-direction:column;justify-content:center;padding-left:7px;padding-right:54px;
  }
  .item-name{
    font-family:"Sorts Mill Goudy",serif;font-size:17px;color:var(--white);line-height:1;
    white-space:nowrap;-webkit-text-stroke:.45px var(--white);
    text-shadow:1px 1px 1px rgba(0,0,0,.35);
  }
  .item-name.tight{font-size:16px;letter-spacing:-.2px;}
  .item-name.two-line{font-size:16.5px;line-height:.98;}
  .item-new{font-family:"Sorts Mill Goudy",serif;font-size:9px;color:var(--white);line-height:1;margin-top:2px;}
  .item-new.inline{display:inline;font-size:10px;-webkit-text-stroke:0;}
  .item-price{
    position:absolute;right:0;top:0;width:56px;height:46px;
    background:linear-gradient(180deg,var(--gold-light) 0%,var(--gold) 55%,var(--gold-dark) 100%);
    clip-path:polygon(0 50%,18px 0,100% 0,100% 100%,18px 100%);
    font-family:"Sorts Mill Goudy",serif;color:var(--red-dark);
    font-size:32px;line-height:46px;text-align:right;padding-right:6px;
    -webkit-text-stroke:.4px var(--red-dark);
  }
  .item-price.small{font-size:27px;}
  .item-price.smaller{font-size:23px;padding-right:3px;}
  .item-desc{
    margin-top:4px;padding-left:7px;width:240px;
    font-size:9.4px;font-weight:300;color:var(--ink);line-height:11px;
  }
  .col-left{left:644px;}
  .col-right{left:916px;}
  .menu-note{
    position:absolute;left:760px;width:280px;top:825px;text-align:center;
    font-size:8.6px;color:var(--red);line-height:1.2;
  }
</style>
</head>
<body>
<main class="menu-spread">

  <section class="cover-page">
    <div class="brand-top">
      <div class="brand-name">Brindle Wokery</div>
      <div class="brand-tagline">Healthy and Original Cooking</div>
    </div>

    <svg class="feature-photo" viewBox="0 0 332 332" role="img" aria-label="Collage of Thai dishes: fried wings, stir-fried vegetables, a dessert with whipped cream and cherry, noodles and fried rice">
      <defs>
        <radialGradient id="photoTones" cx="50%" cy="50%" r="60%">
          <stop offset="0%" stop-color="#e9ddd0"/>
          <stop offset="35%" stop-color="#b8703a"/>
          <stop offset="70%" stop-color="#7a3a1c"/>
          <stop offset="100%" stop-color="#4a3a20"/>
        </radialGradient>
      </defs>
      <polygon points="97,2 235,2 330,97 330,235 235,330 97,330 2,235 2,97"
               fill="url(#photoTones)" stroke="#8e0a0a" stroke-width="3"/>
    </svg>
    <div class="photo-shadow"></div>

    <div class="brand-panel">
      <div class="brand-name">Brindle Wokery</div>
      <div class="brand-tagline">Healthy and Original Cooking</div>
    </div>
  </section>

  <section class="appetizers-page">
    <svg class="section-banner" viewBox="0 0 272 86" aria-hidden="true">
      <polygon points="0,48 40,40 52,74 12,80 22,64" fill="#b0121a"/>
      <polygon points="272,48 232,40 220,74 260,80 250,64" fill="#b0121a"/>
      <polygon points="40,40 52,74 60,66" fill="#6a0808"/>
      <polygon points="232,40 220,74 212,66" fill="#6a0808"/>
      <path d="M36,26 Q136,-2 236,26 L224,66 Q136,40 48,66 Z" fill="#d2181e"/>
      <path d="M36,26 Q136,-2 236,26" fill="none" stroke="#f0d890" stroke-width="1.5"/>
      <path d="M48,66 Q136,40 224,66" fill="none" stroke="#f0d890" stroke-width="1.5"/>
    </svg>
    <div class="section-title">Appetizers</div>

    <!-- Left column -->
    <article class="menu-item col-left" style="top:146px">
      <div class="item-bar"><div class="item-name">Chicken Satay (6)</div><div class="item-price">9</div></div>
      <p class="item-desc">Marinated chicken on skewers served with our famous peanut sauce and cucumber salad.</p>
    </article>
    <article class="menu-item col-left" style="top:238px">
      <div class="item-bar"><div class="item-name">Coconut Shrimp (6)</div><div class="item-new">New!</div><div class="item-price">8</div></div>
      <p class="item-desc">Served with sweet spicy dipping sauce.</p>
    </article>
    <article class="menu-item col-left" style="top:318px">
      <div class="item-bar"><div class="item-name">Brindle Sampler</div><div class="item-price">14</div></div>
      <p class="item-desc">2 Chicken Satay, 2 Golden Shrimp, 2 Pot Stickers,<br>2 Crab Rangoon, and 2 Crispy Spring Roll.</p>
    </article>
    <article class="menu-item col-left" style="top:407px">
      <div class="item-bar"><div class="item-name">Three Musketeers (V)</div><div class="item-new">New!</div><div class="item-price">9</div></div>
      <p class="item-desc">2 Awesome Taro, 2 Sweet Corn Cakes, and 2<br>Crispy Tofu. All Vegetarians!</p>
    </article>
    <article class="menu-item col-left" style="top:497px">
      <div class="item-bar"><div class="item-name">Fried Calamari</div><div class="item-price">8</div></div>
      <p class="item-desc">Battered calamari served with plum sauce.</p>
    </article>
    <article class="menu-item col-left" style="top:575px">
      <div class="item-bar"><div class="item-name">Crab Rangoon (6)</div><div class="item-price small">7.5</div></div>
      <p class="item-desc">Crab with cream cheese in crispy wonton skin</p>
    </article>
    <article class="menu-item col-left" style="top:654px">
      <div class="item-bar"><div class="item-name">Fish Cake (6)<span class="item-new inline">New!</span></div><div class="item-price">8</div></div>
      <p class="item-desc">Thai-style spicy fishcake served with cucumber<br>vinaigrette</p>
    </article>
    <article class="menu-item col-left" style="top:743px">
      <div class="item-bar"><div class="item-name">Thai Beef Jerky</div><div class="item-price">9</div></div>
      <p class="item-desc">Sliced fried beef marinated with Thai seasoning,<br>served with flavorful dipping sauce</p>
    </article>

    <!-- Right column -->
    <article class="menu-item col-right" style="top:146px">
      <div class="item-bar"><div class="item-name tight">Sweet Corn cake (5)(V)</div><div class="item-price small">7.5</div></div>
      <p class="item-desc">Seasoned sweet corn battered and deep-fried<br>served with sweet sauce</p>
    </article>
    <article class="menu-item col-right" style="top:238px">
      <div class="item-bar"><div class="item-name two-line">Chicken or Tofu<br>Lettuce Wrap (V)</div><div class="item-price">9</div></div>
      <p class="item-desc">Minced chicken or tofu, water chestnuts,<br>mushrooms, scallions, crispy noodlesand cool<br>lettucecups with spicy lime sauce</p>
    </article>
    <article class="menu-item col-right" style="top:331px">
      <div class="item-bar"><div class="item-name two-line">Crispy Soft Shell Crabs<br>(2)</div><div class="item-price">8</div></div>
      <p class="item-desc">Soft shell crabs fried to a light crisp served with<br>sweet and spicy sauce</p>
    </article>
    <article class="menu-item col-right" style="top:407px">
      <div class="item-bar"><div class="item-name">Pot Stickers (8)</div><div class="item-price small">7.5</div></div>
      <p class="item-desc">Pork and cabbage dumplings served steamed or<br>fried</p>
    </article>
    <article class="menu-item col-right" style="top:497px">
      <div class="item-bar"><div class="item-name two-line">Mixed Vegetable<br>Tempura (V)</div><div class="item-price">9</div></div>
      <p class="item-desc">Breaded green beans, eggplant, carrot, and<br>broccoli served with Thai ginger sauce</p>
    </article>
    <article class="menu-item col-right" style="top:575px">
      <div class="item-bar"><div class="item-name">Cucumber Salad (V)</div><div class="item-price">5</div></div>
      <p class="item-desc">Sliced cucumber in sweet vinaigrette</p>
    </article>
    <article class="menu-item col-right" style="top:654px">
      <div class="item-bar"><div class="item-name">Edamame(V)</div><div class="item-price">5</div></div>
      <p class="item-desc">Steamed salted soybeans</p>
    </article>
    <article class="menu-item col-right" style="top:743px">
      <div class="item-bar"><div class="item-name tight">Crispy Spring Rolls (5)</div><div class="item-price smaller">7.50</div></div>
      <p class="item-desc">Pork, carrot, cabbage, and noodles in Thai spring<br>roll wrapper Vegetarian Spring Rolls (5) &nbsp;(V)</p>
    </article>

    <p class="menu-note">(V) for Vegetarian. No substitute please.<br>Up to 5 credit card per check, thank you.</p>
  </section>

</main>
</body>
</html>
```